brisknest

i want to ues this logo and the same colors used on the business card

cleaning & service

Industry/Entity Type

Business

Contact Information for Business Card

Font styles to use
Serif
Sans Serif
Decorative
Script

Colors
add136
0692cd
000000
5c5c5c
fbfbfb

Requirements
Must have
• cleaning things

```html
<!DOCTYPE html>
<html lang="en">
<head>
<meta charset="utf-8">
<title>brisknest business card</title>
<link href="https://fonts.googleapis.com/css2?family=Work+Sans:wght@400;600&display=swap" rel="stylesheet">
<style>
  :root {
    --green: #add136;
    --blue: #0692cd;
    --blue-deep: #0b6fbf;
    --ink: #5c5c5c;
    --black: #000000;
    --paper: #fbfbfb;
    --backdrop: #1d1d1f;
    --mark-light: #eef0ea;
  }
  * { margin: 0; padding: 0; box-sizing: border-box; }
  html, body { width: 1200px; height: 963px; overflow: hidden; }
  body {
    background: var(--backdrop);
    font-family: "Work Sans", Arial, sans-serif;
    display: flex;
    align-items: center;
    justify-content: center;
    gap: 40px;
  }
  .card {
    width: 540px;
    height: 309px;
    border-radius: 16px;
    position: relative;
    overflow: hidden;
  }
  /* front */
  .card-front { background: var(--paper); }
  .brand {
    position: absolute;
    left: 34px;
    top: 118px;
    width: 168px;
    display: flex;
    align-items: center;
    gap: 8px;
    color: var(--blue-deep);
    font-weight: 600;
    font-size: 28px;
  }
  .brand-dot {
    width: 14px; height: 14px; border-radius: 50%;
    background: var(--green);
    flex: none;
  }
  .divider {
    position: absolute;
    left: 222px; top: 62px;
    width: 1.5px; height: 150px;
    background: var(--blue-deep);
  }
  .details {
    position: absolute;
    left: 250px; top: 62px;
    color: var(--ink);
    font-size: 13px;
    line-height: 1.45;
  }
  .person-name {
    color: var(--blue-deep);
    font-weight: 600;
    font-size: 22px;
    letter-spacing: 0.5px;
    line-height: 1.1;
  }
  .person-role { margin-bottom: 8px; }
  .address { margin-bottom: 6px; }
  .contact-row { display: flex; align-items: center; gap: 7px; }
  .contact-row svg { width: 11px; height: 11px; flex: none; }
  .band-line {
    position: absolute; left: 0; right: 0; bottom: 26px;
    height: 2px; background: var(--green);
  }
  .band {
    position: absolute; left: 0; right: 0; bottom: 0;
    height: 22px; background: var(--blue-deep);
  }
  /* back */
  .card-back {
    background: radial-gradient(circle at 45% 40%, #b4d94a 0%, var(--green) 55%, #94bb2c 100%);
    display: flex; align-items: center; justify-content: center;
  }
  .back-brand {
    display: flex; align-items: center; gap: 12px;
    color: var(--mark-light);
    font-weight: 600;
    font-size: 44px;
  }
  .back-brand .brand-dot { width: 20px; height: 20px; background: var(--mark-light); }
</style>
</head>
<body>
  <section class="card card-front">
    <div class="brand"><span class="brand-dot"></span>brisknest</div>
    <div class="divider"></div>
    <div class="details">
      <p class="person-name">MARLA QUINN</p>
      <p class="person-role">Director</p>
      <p class="address">47 Alder Row,<br>Fenwick ON K1R 2P4</p>
      <p class="contact-row">
        <svg viewBox="0 0 12 12"><path d="M3 1 L5 3.5 L4 5 Q5 7.5 7 8 L8.5 7 L11 9 L9.5 11 Q2 10 1 2.5 Z" fill="#0b6fbf"/></svg>
        +330 5512-9043
      </p>
      <p class="contact-row">
        <svg viewBox="0 0 12 12"><rect x="1" y="2.5" width="10" height="7" fill="none" stroke="#0b6fbf" stroke-width="1.2"/><path d="M1 2.5 L6 6.5 L11 2.5" fill="none" stroke="#0b6fbf" stroke-width="1.2"/></svg>
        info@brisknest.com
      </p>
      <p class="contact-row">
        <svg viewBox="0 0 12 12"><circle cx="6" cy="6" r="5" fill="none" stroke="#0692cd" stroke-width="1.2"/><path d="M1 6 H11 M6 1 Q3 6 6 11 M6 1 Q9 6 6 11" fill="none" stroke="#0692cd" stroke-width="1"/></svg>
        www.brisknest.com
      </p>
    </div>
    <div class="band-line"></div>
    <div class="band"></div>
  </section>

  <section class="card card-back">
    <div class="back-brand"><span class="brand-dot"></span>brisknest</div>
  </section>
</body>
</html>
```